Open Doors Sermon Series

Design a 4x6 Double Sides Digital Postcard for our new sermon series...begins Sunday.

Here is info on the Sermon Series:

Sermon Series Title: Open Doors

Sermon Series Description: The goal of the “Open Doors” series is to turn followers into fishermen. If you’ve ever gone fishing, then you know that one of the most exciting feelings in the world is that underwater tug on the other end of the line. That is the feeling true fishermen get hooked on and want to experience again and again.
Our Lord Jesus and his fishermen disciples knew all about that. In Matthew 4:19, Jesus gave a different kind of fishing invitation to two brothers who were casting nets into the sea. He said, “Follow me, and I will make you fishers of men.”
Modern day disciples are still being found by Jesus and accepting his invitation to find people for Jesus. Are you one of them? As we prepare to move to our new church home, it takes found people to find people and invite them to church. So come and learn how to cast your own net and what to do when you feel the tug of the BIG ONE.

Assignments:
June 1, 2014 - Walk With Open Hands
June 8, 2014 - Hunger for a Harvest
June 15, 2014 - Father's Day
June 22, 2014 - The Far End of the Valley

Worship Times:
9:55 AM - Traditional Worship
12:00 PM - Contemporary Worship

Church name: Maplecrest Road Congregational Church

Leadership:
Rev. Delphine Harlow Okafor, Senior Pastor & Teacher

Contact Information:
4100 Maplecrest Rd.
Cleveland, OH 44115
216.555.0148
www.mrcc-ps.example

```html
<!DOCTYPE html>
<html lang="en">
<head>
<meta charset="utf-8">
<title>Open Doors Sermon Series Postcard</title>
<link href="https://fonts.googleapis.com/css2?family=Cinzel:wght@600&family=Open+Sans:wght@400;600;700&family=Roboto+Condensed:wght@700&family=Ubuntu:wght@400&display=swap" rel="stylesheet">
<style>
  :root {
    --backdrop: #4a1d16;
    --card-white: #ffffff;
    --ink: #111111;
    --highlight: #f3ef7a;
    --stamp: #f3f2f2;
    --sky-mist: #dfe9ee;
    --sunset-gold: #ffd23c;
    --sunset-orange: #e8561a;
    --sunset-red: #9a1c10;
    --hill-dark: #1c1210;
    --label-red: #b31e12;
    --name-gold: #f6b23a;
    --text-light: #ffffff;
  }
  * { margin: 0; padding: 0; box-sizing: border-box; }
  html, body { width: 1200px; height: 1000px; overflow: hidden; }
  body { background: var(--backdrop); position: relative; font-family: "Open Sans", sans-serif; }

  /* Back of postcard */
  .card-back {
    position: absolute; left: 56px; top: 68px; width: 649px; height: 503px;
    background: var(--card-white); overflow: hidden; color: var(--ink);
  }
  .gate-scene {
    position: absolute; left: 0; top: 0; width: 360px; height: 460px;
    background:
      radial-gradient(ellipse at 35% 20%, rgba(255,255,255,0.9), rgba(255,255,255,0) 60%),
      linear-gradient(90deg, var(--sky-mist) 0%, rgba(223,233,238,0.6) 60%, rgba(255,255,255,0) 100%);
  }
  .back-title {
    position: absolute; left: 170px; width: 314px; top: 41px; text-align: center;
    font-weight: 700; font-size: 20px; line-height: 27px; letter-spacing: 0;
  }
  .back-leadership {
    position: absolute; left: 170px; width: 314px; top: 104px; text-align: center;
    font-size: 11px; line-height: 15px; font-weight: 600;
  }
  .stamp-box { position: absolute; left: 499px; top: 29px; width: 123px; height: 118px; background: var(--stamp); }
  .label-band {
    position: absolute; left: 46px; height: 24px; padding-left: 12px;
    background: var(--highlight); font-size: 13.5px; line-height: 24px; font-weight: 600;
  }
  .label-assignments { top: 172px; width: 131px; }
  .label-worship { top: 284px; width: 122px; }
  .back-list { position: absolute; left: 58px; font-size: 13px; line-height: 16px; list-style: none; }
  .assignment-list { top: 209px; }
  .worship-list { top: 321px; }
  .call-line {
    position: absolute; left: 31px; top: 360px;
    font-family: "Roboto Condensed", sans-serif; font-weight: 700; font-size: 26px; letter-spacing: -0.3px;
  }
  .back-web { position: absolute; left: 107px; top: 392px; font-size: 11px; }

  /* Front of postcard */
  .card-front {
    position: absolute; left: 491px; top: 425px; width: 656px; height: 508px; overflow: hidden; color: var(--text-light);
  }
  .sunset-scene {
    position: absolute; inset: 0;
    background:
      radial-gradient(circle at 21% 38%, #fff7c8 0%, var(--sunset-gold) 8%, rgba(255,160,40,0.7) 22%, rgba(232,86,26,0) 45%),
      linear-gradient(180deg, var(--sunset-red) 0%, var(--sunset-orange) 28%, #c63a14 45%, var(--hill-dark) 62%, #120c0b 100%);
  }
  .front-title {
    position: absolute; left: 0; width: 656px; top: 30px; text-align: center;
    font-family: "Ubuntu", sans-serif; font-weight: 400; font-size: 22px; color: var(--ink);
  }
  .series-label { position: absolute; left: 0; width: 656px; top: 64px; text-align: center; font-size: 13.5px; color: var(--ink); }
  .series-name {
    position: absolute; left: 0; width: 656px; top: 82px; text-align: center;
    font-family: "Cinzel", serif; font-weight: 600; font-size: 40px; color: var(--card-white);
    text-shadow: 0 1px 2px rgba(60,20,0,0.5);
  }
  .pastor-portrait {
    position: absolute; left: 530px; top: 77px; width: 84px; height: 111px;
    border: 2px solid var(--card-white); background: linear-gradient(180deg, #8a8f8a, #5d6360);
  }
  .front-leadership {
    position: absolute; right: 32px; top: 196px; text-align: right; font-size: 12px; line-height: 15px;
  }
  .front-leadership .label { color: var(--label-red); }
  .front-leadership .name { color: var(--name-gold); }
  .series-description {
    position: absolute; left: 30px; width: 600px; top: 266px; font-size: 11px; line-height: 12.6px;
  }
  .series-description p + p { margin-top: 12.6px; }
  .front-contact {
    position: absolute; left: 0; width: 656px; top: 443px; text-align: center; font-size: 14px;
  }
  .front-contact svg { vertical-align: -2px; margin: 0 6px 0 10px; }
  .front-web { position: absolute; left: 0; width: 656px; top: 465px; text-align: center; font-size: 10px; }
</style>
</head>
<body>

<section class="card-back">
  <div class="gate-scene" role="img" aria-label="Heavenly gates in clouds beneath a golden cross"></div>
  <h1 class="back-title">MAPLECREST ROAD<br>CONGREGATIONAL CHURCH</h1>
  <p class="back-leadership">LEADERSHIP:<br>REV. DELPHINE HARLOW OKAFOR,<br>SENIOR PASTOR &amp; TEACHER</p>
  <div class="stamp-box"></div>

  <div class="label-band label-assignments">Assignments:</div>
  <ul class="back-list assignment-list">
    <li>June 1, 2014 - Walk With Open Hands</li>
    <li>June 8, 2014 - Hunger for a Harvest</li>
    <li>June 15, 2014 - Father's Day</li>
    <li>June 22, 2014 - The Far End of the Valley</li>
  </ul>

  <div class="label-band label-worship">Worship Times:</div>
  <ul class="back-list worship-list">
    <li>9:55 AM - Traditional Worship</li>
    <li>12:00 PM - Contemporary Worship</li>
  </ul>

  <p class="call-line">Call Us Now 216.555.0148</p>
  <p class="back-web">www.mrcc-ps.example</p>
</section>

<section class="card-front">
  <div class="sunset-scene" role="img" aria-label="Three crosses on a hill against a glowing sunset"></div>
  <h2 class="front-title">MAPLECREST ROAD CONGREGATIONAL CHURCH</h2>
  <p class="series-label">SERMON SERIES</p>
  <p class="series-name">Open Doors</p>
  <div class="pastor-portrait" role="img" aria-label="Portrait of the senior pastor"></div>
  <p class="front-leadership"><span class="label">Leadership:</span>&nbsp; <span class="name">Rev. Delphine Harlow Okafor,<br>Senior Pastor &amp; Teacher</span></p>

  <div class="series-description">
    <p>The goal of the “Open Doors” series is to turn followers into fishermen. If you’ve ever gone fishing, then you know that one of the most exciting feelings in the world is that underwater tug on the other end of the line. That is the feeling true fishermen get hooked on and want to experience again and again.</p>
    <p>Our Lord Jesus and his fishermen disciples knew all about that. In Matthew 4:19, Jesus gave a different kind of fishing invitation to two brothers who were casting nets into the sea. He said, “Follow me, and I will make you fishers of men.”</p>
    <p>Modern day disciples are still being found by Jesus and accepting his invitation to find people for Jesus. Are you one of them? As we prepare to move to our new church home, it takes found people to find people and invite them to church. So come and learn how to cast your own net and what to do when you feel the tug of the BIG ONE.</p>
  </div>

  <p class="front-contact">Contact Information :&nbsp; 4100 Maplecrest Rd. Cleveland, OH 44115<svg width="14" height="12" viewBox="0 0 14 12" aria-hidden="true"><path d="M1 4 Q7 -1 13 4 L11 5.5 L9.5 3.5 L4.5 3.5 L3 5.5 Z" fill="var(--sunset-gold)"/><rect x="3" y="6" width="8" height="5" rx="1" fill="var(--sunset-gold)"/></svg>216.555.0148</p>
  <p class="front-web">www.mrcc-ps.example</p>
</section>

</body>
</html>
```